Quillon - Energy management company website design

We are interested in a total redesign of our website at www.quillonpowerco.co.uk. We are happy with our current colour scheme and logo but are ready for a new website.

The site is running on a CMS called Umbraco and will remain on this CMS. We are just looking for the html/css and js files so I can build the templates.

We are looking for a home page and maybe a couple of different types of content page. We would like the site to look clean and professional but not necessarily like every other corporate website.
We are really open to any design ideas, we've left the brief quite ambiguous for that reason. We are happy to consider any design no matter how unorthodox as long as it remains professional.

Target Market(s)

Large Businesses

Industry/Entity Type

It Company

Coding

Coded - Design and coding required

Number of Pages Required

3 page

Font styles to use
Sans Serif

Requirements
Must have
• We need a landing page designed and possibly two different kinds of content page allowing for different styles of content. We will want the css and js code with the pages.
• On the home page we would like Two prominent articles/products.
• Then a selection of our other products/services.
• Testimonials, Case studies and News Articles.
• Company colours:
• Text and topleft arrow blue (dark):
• R: 0 G: 96 B: 167
• Red Text and Arrow:
• R: 237 G: 27 B: 35
• Bottom left arrow blue (medium):
• R: 0 G: 174 B: 239
• Bottom right arrow blue (light):
• R: 171 G: 225 B: 250
Nice to have
• We are open to a potentially radical redesign of the site, it doesn't necessarily need to look like every other corporate website.
• We would like to see one or two designs base on this type of imagery:
• http://vuz.lk/PaRmet
• http://vuz.lk/3Hbxno
• http://vuz.lk/K4FUdj

```html
<!DOCTYPE html>
<html lang="en">
<head>
<meta charset="utf-8">
<title>Quillon – Integrated Energy Experts</title>
<link rel="stylesheet" href="https://fonts.googleapis.com/css2?family=Raleway:ital,wght@0,300;0,400;0,500;0,600;0,700;1,400;1,600&display=swap">
<style>
:root{
  --blue-dark:#0060a7;
  --red:#ed1b23;
  --blue-mid:#00aeef;
  --blue-light:#abe1fa;
  --ink:#222;
  --muted:#333;
  --panel:#efefef;
  --card-head:#f0f0f0;
  --services-a:#0d4f97;
  --services-b:#1c6ab4;
  --footer:#eef0f3;
  --bar:#a7a7a7;
}
*{box-sizing:border-box;margin:0;padding:0}
html,body{width:1200px;height:2601px;overflow:hidden}
body{font-family:"Raleway",sans-serif;color:var(--ink);background:#fff;position:relative}
.abs{position:absolute}

/* header */
.site-header{position:absolute;left:0;top:0;width:1200px;height:121px;background:#fff;border-top:4px solid var(--red);border-bottom:5px solid var(--blue-dark)}
.brand{position:absolute;left:43px;top:34px;display:flex;align-items:center;gap:12px}
.brand-dot{width:44px;height:44px;border-radius:50%;background:var(--blue-dark)}
.brand-name{font-size:38px;font-weight:700;color:var(--blue-dark);letter-spacing:1px}
.header-phone{position:absolute;right:50px;top:26px;font-size:13px;display:flex;align-items:center;gap:8px}
.main-nav{position:absolute;right:50px;top:74px;display:flex;gap:24px;font-size:13px;font-weight:700}
.main-nav a{color:#111;text-decoration:none}
.main-nav a.is-active{color:var(--red)}

/* hero */
.hero{position:absolute;left:0;top:121px;width:1200px;height:599px;overflow:hidden}
.hero-visual{position:absolute;inset:0;background:radial-gradient(ellipse at 30% 45%,#2f6fb8 0%,#10213d 30%,transparent 55%),radial-gradient(ellipse at 68% 40%,#e79a3a 0%,#6a2a10 28%,transparent 55%),#050608}
.hero-title{position:absolute;left:0;top:62px;width:1200px;text-align:center;color:#fff;font-weight:300;font-size:31px;line-height:38px}
.hero-call{position:absolute;left:83px;top:512px;color:#fff;font-size:31px;font-weight:400}
.hero-arrow{position:absolute;top:290px;width:28px;height:32px;background:#2a2310;border:1px solid #6b5a28;display:flex;align-items:center;justify-content:center}

/* about */
.about{position:absolute;left:0;top:720px;width:1200px;height:350px;background:var(--panel)}
.about-mark{position:absolute;left:83px;top:52px;width:182px;height:182px}
.about-title{position:absolute;left:343px;top:60px;font-size:33px;font-weight:400}
.about-text{position:absolute;left:343px;top:106px;width:595px;font-size:13px;line-height:22px;color:var(--muted)}
.btn{display:inline-block;background:var(--red);color:#fff;font-size:13px;text-align:center;text-decoration:none}
.about .btn{position:absolute;left:343px;top:249px;width:125px;height:26px;line-height:26px}

/* services */
.services{position:absolute;left:0;top:1070px;width:1200px;height:907px;background:linear-gradient(160deg,var(--services-b),var(--services-a) 55%,#124f93)}
.section-title{position:absolute;left:0;width:1200px;text-align:center;font-size:33px;font-weight:400}
.services .section-title{top:26px;color:#fff}
.card{position:absolute;background:#fff;width:314px;height:216px}
.card-head{height:54px;background:var(--card-head);font-size:21px;line-height:54px;padding-left:17px;color:#333}
.card-img{position:absolute;left:12px;top:66px;width:96px;height:97px}
.card-text{position:absolute;left:125px;top:68px;width:170px;font-size:13px;line-height:16.3px;color:var(--muted)}
.card .btn{position:absolute;right:0;bottom:0;width:100px;height:26px;line-height:26px}
.card-wide{width:498px}
.card-wide .card-text{width:355px}
.customers-nav{position:absolute;right:14px;top:18px;display:flex;gap:8px;color:#999;font-size:18px}
.customer-grid{position:absolute;left:22px;top:78px;width:460px;display:grid;grid-template-columns:repeat(3,1fr);row-gap:34px;column-gap:12px}
.customer-name{display:flex;align-items:center;gap:8px;font-size:18px;font-weight:600;color:var(--blue-dark)}
.customer-name i{display:block;width:14px;height:14px;background:var(--blue-dark)}
.customer-name.alt{color:#444}
.customer-name.alt i{background:var(--red)}

/* testimonials */
.testimonials{position:absolute;left:0;top:1977px;width:1200px;height:390px;background:#fff}
.testimonials .section-title{top:40px;color:#333}
.quote-card{position:absolute;top:121px;width:497px;height:212px;background:#eef1f4;border-bottom:2px solid var(--red)}
.quote-photo{position:absolute;left:0;top:0;width:179px;height:144px}
.quote-fold{position:absolute;left:0;top:144px}
.quote-text{position:absolute;left:203px;top:17px;width:270px;font-size:13px;line-height:16px;color:#333}
.quote-cite{position:absolute;left:203px;top:150px;font-size:13px;line-height:16px;font-style:italic;color:#333}
.quote-cite strong{font-weight:600}

/* footer */
.site-footer{position:absolute;left:0;top:2367px;width:1200px;height:196px;background:var(--footer);border-top:2px solid var(--blue-dark)}
.footer-brand{position:absolute;left:43px;top:22px;display:flex;align-items:center;gap:12px}
.footer-brand .brand-dot{width:38px;height:38px}
.footer-brand .brand-name{font-size:33px}
.footer-address{position:absolute;left:83px;top:92px;font-size:12.5px;line-height:16px;color:#333}
.social{position:absolute;left:83px;top:152px;display:flex;gap:10px}
.social span{width:26px;height:26px;border-radius:50%;background:#1c7fc8}
.footer-col{position:absolute;top:32px;font-size:12.5px;line-height:17.5px;color:#333}
.footer-col h3{font-size:12.5px;font-weight:700;margin-bottom:4px;color:#222}
.footer-map{position:absolute;left:881px;top:53px;width:267px;height:122px;background:linear-gradient(135deg,#e6ecd8,#dfe6ea 60%,#e8e3d2)}
.footer-bar{position:absolute;left:0;top:2563px;width:1200px;height:38px;background:var(--bar);color:#fff;font-size:12px;line-height:38px}
.footer-bar .copy{position:absolute;left:43px}
.footer-bar .legal{position:absolute;right:50px}
</style>
</head>
<body>

<header class="site-header">
  <div class="brand"><span class="brand-dot"></span><span class="brand-name">Quillon</span></div>
  <div class="header-phone">
    <svg width="14" height="14" viewBox="0 0 24 24" aria-hidden="true"><path fill="#111" d="M6.6 10.8a15 15 0 0 0 6.6 6.6l2.2-2.2c.3-.3.7-.4 1-.2 1.1.4 2.3.6 3.6.6.6 0 1 .4 1 1V20c0 .6-.4 1-1 1A17 17 0 0 1 3 4c0-.6.4-1 1-1h3.5c.6 0 1 .4 1 1 0 1.3.2 2.5.6 3.6.1.3 0 .7-.2 1z"/></svg>
    0845 210 7730
  </div>
  <nav class="main-nav">
    <a href="#" class="is-active">HOME</a>
    <a href="#">OUR SERVICES</a>
    <a href="#">OUR CUSTOMERS</a>
    <a href="#">PULSE</a>
    <a href="#">COMPANY</a>
    <a href="#">CONTACT US</a>
  </nav>
</header>

<section class="hero">
  <div class="hero-visual" role="img" aria-label="Clenched fist gripping crackling blue and orange electric lightning on a dark background"></div>
  <h1 class="hero-title">Quillon’s unique 360 degree service is designed<br>to optimise all areas of your energy and telecom expenditure</h1>
  <p class="hero-call">Call us on: 0845 210 7730</p>
  <a class="hero-arrow" style="left:35px" href="#" aria-label="Previous slide"><svg width="10" height="14" viewBox="0 0 10 14"><path d="M8 1 2 7l6 6" fill="none" stroke="#fff" stroke-width="2"/></svg></a>
  <a class="hero-arrow" style="left:1137px" href="#" aria-label="Next slide"><svg width="10" height="14" viewBox="0 0 10 14"><path d="M2 1l6 6-6 6" fill="none" stroke="#fff" stroke-width="2"/></svg></a>
</section>

<section class="about">
  <svg class="about-mark" viewBox="0 0 182 182" role="img" aria-label="Service cycle emblem">
    <circle cx="91" cy="91" r="91" fill="var(--blue-dark)"/>
  </svg>
  <h2 class="about-title">About Quillon</h2>
  <p class="about-text">Lorem Ipsum is simply dummy text of the printing and typesetting industry. Lorem Ipsum has been the industry’s standard dummy text ever since the 1500s, when ... unknown printer took a galley of type and scrambled it to make a type specimen book.Lorem Ipsum is simply dummy text of the printing and typesetting industry. Lorem Ipsum has been the industry’s standard dummy text ever since the 1500s, when ... unknown printer took a galley of type and scrambled it to make a type specimen book.</p>
  <a class="btn" href="#">Read More</a>
</section>

<section class="services">
  <h2 class="section-title">Our Services</h2>

  <article class="card" style="left:83px;top:106px">
    <h3 class="card-head">Energy Procurement</h3>
    <div class="card-img" role="img" aria-label="Glowing light bulb over an open hand" style="background:linear-gradient(160deg,#6a8fb8,#1b2c48)"></div>
    <p class="card-text">Lorem Ipsum is simply dummy text of the printing and typesetting industry. Lorem Ipsum has been the industry’s standard dummy text ever since the ...</p>
    <a class="btn" href="#">Read More</a>
  </article>
  <article class="card" style="left:439px;top:106px">
    <h3 class="card-head">Energy Efficiency</h3>
    <div class="card-img" role="img" aria-label="Electricity pylon against a blue sky" style="background:linear-gradient(180deg,#5a8ed0,#1d4f9a)"></div>
    <p class="card-text">Lorem Ipsum is simply dummy text of the printing and typesetting industry. Lorem Ipsum has been the industry’s standard dummy text ever since the ...</p>
    <a class="btn" href="#">Read More</a>
  </article>
  <article class="card" style="left:792px;top:106px">
    <h3 class="card-head">Energy Analysis</h3>
    <div class="card-img" role="img" aria-label="Coloured energy rating house shapes" style="background:linear-gradient(90deg,#3c9a3a,#c9c02c,#e8872a,#d23a2a)"></div>
    <p class="card-text">Lorem Ipsum is simply dummy text of the printing and typesetting industry. Lorem Ipsum has been the industry’s standard dummy text ever since the ...</p>
    <a class="btn" href="#">Read More</a>
  </article>

  <article class="card" style="left:83px;top:359px">
    <h3 class="card-head">Energy Compliance</h3>
    <div class="card-img" role="img" aria-label="Hand holding a small glowing globe" style="background:radial-gradient(circle at 50% 55%,#7fb6e0,#11243f 65%)"></div>
    <p class="card-text">Lorem Ipsum is simply dummy text of the printing and typesetting industry. Lorem Ipsum has been the industry’s standard dummy text ever since the ...</p>
    <a class="btn" href="#">Read More</a>
  </article>
  <article class="card" style="left:439px;top:359px">
    <h3 class="card-head">Telecoms</h3>
    <div class="card-img" role="img" aria-label="Finger pressing a telephone keypad" style="background:linear-gradient(150deg,#d8d6d2,#8d8a86)"></div>
    <p class="card-text">Lorem Ipsum is simply dummy text of the printing and typesetting industry. Lorem Ipsum has been the industry’s standard dummy text ever since the ...</p>
    <a class="btn" href="#">Read More</a>
  </article>
  <article class="card" style="left:792px;top:359px">
    <h3 class="card-head">ESOS</h3>
    <div class="card-img" role="img" aria-label="Satellite dish silhouetted against the sky" style="background:linear-gradient(180deg,#a9c6df,#4d6f92)"></div>
    <p class="card-text">Lorem Ipsum is simply dummy text of the printing and typesetting industry. Lorem Ipsum has been the industry’s standard dummy text ever since the ...</p>
    <a class="btn" href="#">Read More</a>
  </article>

  <article class="card card-wide" style="left:83px;top:612px">
    <h3 class="card-head">Public Sector</h3>
    <div class="card-img" role="img" aria-label="Hands exchanging banknotes" style="background:linear-gradient(150deg,#b9c7a2,#5b6d49)"></div>
    <p class="card-text">Lorem Ipsum is simply dummy text of the printing and typesetting industry. Lorem Ipsum has been the industry’s standard dummy text ever since the 1500s, when ... unknown printer took a galley of type and scrambled it to make a type specimen book.Lorem Ipsum is simply dummy text of the printing and typesetting industry.</p>
    <a class="btn" href="#">Read More</a>
  </article>

  <article class="card card-wide" style="left:607px;top:612px">
    <h3 class="card-head">Our Customers</h3>
    <div class="customers-nav" aria-hidden="true"><span>‹</span><span>›</span></div>
    <div class="customer-grid">
      <span class="customer-name"><i></i>Harbourline</span>
      <span class="customer-name"><i></i>Corvane</span>
      <span class="customer-name"><i></i>Eastmoor</span>
      <span class="customer-name alt"><i></i>Brickfeld</span>
      <span class="customer-name alt"><i></i>Alverton</span>
      <span class="customer-name alt"><i></i>Tessaro</span>
    </div>
  </article>
</section>

<section class="testimonials">
  <h2 class="section-title">Customer Testimonials</h2>

  <article class="quote-card" style="left:83px">
    <div class="quote-photo" role="img" aria-label="Portrait of a smiling customer in a light shirt" style="background:linear-gradient(135deg,#bfb2a2,#6f6358)"></div>
    <svg class="quote-fold" width="179" height="68" viewBox="0 0 179 68" aria-hidden="true"><path d="M0 0h179v68z" fill="#c9cccf"/></svg>
    <p class="quote-text">Quillon listened to our needs and delivered a service that was tailored to us. The strategic management of our flexible purchasing contracts has been a great success, their energy conservation expertise has helped us enormously, and we'd have no hesitation recommending their services.</p>
    <p class="quote-cite"><strong>Martin Hale</strong><br>Stadium Manager<br>Riverside Athletic Club</p>
  </article>

  <article class="quote-card" style="left:610px">
    <div class="quote-photo" role="img" aria-label="Portrait of a smiling customer with dark hair" style="background:linear-gradient(135deg,#eeeeee,#b9a89c)"></div>
    <svg class="quote-fold" width="179" height="68" viewBox="0 0 179 68" aria-hidden="true"><path d="M0 0h179v68z" fill="#c9cccf"/></svg>
    <p class="quote-text">Quillon listened to our needs and delivered a service that was tailored to us. The strategic management of our flexible purchasing contracts has been a great success, their energy conservation expertise has helped us enormously, and we'd have no hesitation recommending their services.</p>
    <p class="quote-cite"><strong>Clara Wren</strong><br>Stadium Manager<br>Riverside Athletic Club</p>
  </article>
</section>

<footer class="site-footer">
  <div class="footer-brand"><span class="brand-dot"></span><span class="brand-name">Quillon</span></div>
  <p class="footer-address">Quillon Utilities Ltd<br>Quillon House, Marsh Lane Drive<br>Fleetmouth, FL4 2QD</p>
  <div class="social" aria-label="Social links"><span></span><span></span></div>

  <div class="footer-col" style="left:484px">
    <h3>Navigations</h3>
    About Us<br>Our Customers<br>Quillon Energy View<br>Contact Us
  </div>
  <div class="footer-col" style="left:668px">
    <h3>Our Services</h3>
    Energy Procurement<br>Energy Efficiency<br>Energy Analysis<br>Energy Compliance<br>Telecoms<br>ESOS<br>Public Sector
  </div>
  <div class="footer-col" style="left:881px">
    <h3>Our Location</h3>
  </div>
  <div class="footer-map" role="img" aria-label="Street map showing the office location"></div>
</footer>
<div class="footer-bar">
  <span class="copy">© 2013 Quillon Utilities Limited</span>
  <span class="legal">Privacy Policy &nbsp;|&nbsp; Disclaimer</span>
</div>

</body>
</html>
```